Retail Sign for Houseplant Campaign

Sign will measure 3 to 4 foot tall by 22.2inches and place on rolling racks of houseplants for a retail promotion in The Brickfield Yard. The theme of the promotion will be "New Year, New You!" Selling points which should be on the sign are Houseplants give you a taste of nature, Houseplants boost air quality inside your home, Indoor plants reduce anxiety, Indoor plants make you more productive, Houseplants improve your concentration and memory.
Updates

Target Market(s)

People who love plants

Industry/Entity Type

Horticulture/ retail

Colors
00AB8E
00BBA5
67D7C9
C6EFE9
E9F9F6
59FF00
82FF00
B8FF75
E3FFCB
F4FFEA
FFF300
FFF600
FEFA6F
FFFEC7
FFFEE8

Requirements
Must have
• Must feel energetic and encourage people to buy plants. Should include 1-2 photos and the selling points listed

```html
<!DOCTYPE html>
<html lang="en">
<head>
<meta charset="utf-8">
<title>New Year, New You – Houseplant Sign</title>
<link rel="stylesheet" href="https://fonts.googleapis.com/css2?family=Italiana&family=Nunito:wght@800;900&display=swap">
<style>
  :root {
    --backdrop: #eef3e6;
    --paper: #ffffff;
    --leaf-green: #84bb41;
    --frond-green: #4f8f3a;
    --band-lime: #d3db24;
    --ink-green: #2f6a2a;
    --ring-lime: #c9dc2a;
    --photo-light: #e9ece4;
    --photo-leaf: #2f5a2c;
  }
  * { box-sizing: border-box; margin: 0; padding: 0; }
  html, body {
    width: 1200px; height: 1200px; overflow: hidden;
    background: var(--backdrop);
  }
  .sign {
    position: absolute; left: 243px; top: 30px;
    width: 713px; height: 1140px;
    background: var(--paper);
    overflow: hidden;
  }
  .sign__panel {
    position: absolute; left: 22px; top: 20px;
    width: 669px; height: 1095px;
    background: var(--leaf-green);
    overflow: hidden;
  }
  .fronds {
    position: absolute;
  }
  .fronds--right {
    left: 400px; top: 140px; width: 269px; height: 570px;
    background: radial-gradient(ellipse at 80% 60%, rgba(79,143,58,0.7) 0%, rgba(79,143,58,0.3) 45%, rgba(79,143,58,0) 70%);
  }
  .fronds--left {
    left: 0; top: 560px; width: 320px; height: 150px;
    background: radial-gradient(ellipse at 30% 90%, rgba(79,143,58,0.6) 0%, rgba(79,143,58,0.25) 45%, rgba(79,143,58,0) 70%);
  }
  .fronds--bottom {
    left: 0; top: 970px; width: 300px; height: 125px;
    background: radial-gradient(ellipse at 35% 40%, rgba(79,143,58,0.7) 0%, rgba(79,143,58,0.3) 50%, rgba(79,143,58,0) 72%);
  }
  .headline {
    position: absolute; left: 46px; top: 44px;
    font-family: "Italiana", serif;
    font-weight: 400;
    font-size: 128px;
    line-height: 142px;
    color: var(--paper);
    letter-spacing: -6px;
    white-space: nowrap;
  }
  .photo {
    position: absolute;
    border-radius: 50%;
    border: 3px solid var(--ring-lime);
  }
  .photo--plant-care {
    left: 40px; top: 352px; width: 333px; height: 333px;
    background: linear-gradient(100deg, var(--photo-light) 0%, #f4f3ef 45%, #5d7f4e 70%, var(--photo-leaf) 100%);
  }
  .photo--repotting {
    left: 431px; top: 365px; width: 232px; height: 232px;
    background: linear-gradient(90deg, #e6e1d6 0%, #f2efe9 45%, #d9bfa3 75%, #efece6 100%);
  }
  .facts {
    position: absolute; left: 0; top: 729px;
    width: 713px; height: 261px;
    background: var(--band-lime);
  }
  .facts__title {
    position: absolute; left: 62px; top: 24px;
    font-family: "Italiana", serif;
    font-size: 42px;
    line-height: 48px;
    letter-spacing: -1.5px;
    color: var(--paper);
    -webkit-text-stroke: 0.6px var(--paper);
    white-space: nowrap;
  }
  .facts__list {
    position: absolute; left: 54px; top: 90px;
    list-style: none;
    font-family: "Nunito", sans-serif;
    font-weight: 900;
    font-size: 17.5px;
    line-height: 31.7px;
    color: var(--ink-green);
    text-transform: uppercase;
    letter-spacing: 0;
    white-space: nowrap;
  }
  .facts__list li::before { content: "\2022\00a0"; }
  .partners {
    position: absolute; left: 489px; top: 928px;
    width: 172px; height: 172px;
    border-radius: 50%;
    background: var(--paper);
    border: 2px solid var(--frond-green);
    display: flex; flex-direction: column;
    align-items: center; justify-content: center;
    gap: 16px;
    font-family: "Nunito", sans-serif;
    font-weight: 800;
    color: var(--ink-green);
    text-align: center;
  }
  .partners__brand { font-size: 16px; line-height: 18px; }
  .partners__store { font-size: 15px; line-height: 17px; }
</style>
</head>
<body>
  <main class="sign">
    <div class="sign__panel">
      <div class="fronds fronds--right" role="img" aria-label="Palm frond illustration"></div>
      <div class="fronds fronds--left" role="img" aria-label="Palm frond illustration"></div>
      <div class="fronds fronds--bottom" role="img" aria-label="Palm frond illustration"></div>
    </div>

    <h1 class="headline">NEW YEAR,<br>NEW YOU</h1>

    <div class="photo photo--plant-care" role="img" aria-label="Photo of a smiling woman wiping a monstera leaf"></div>
    <div class="photo photo--repotting" role="img" aria-label="Photo of a woman potting a croton plant at a table"></div>

    <section class="facts">
      <h2 class="facts__title">DID YOU KNOW?</h2>
      <ul class="facts__list">
        <li>Houseplants give you a taste of nature</li>
        <li>Houseplants improve your concentration &amp; memory</li>
        <li>Houseplants boost air quality inside your home</li>
        <li>Indoor plants make you more productive</li>
        <li>Indoor plants reduce anxiety</li>
      </ul>
    </section>

    <div class="partners">
      <span class="partners__brand">VERDANT ROOTS</span>
      <span class="partners__store">THE BRICKFIELD<br>YARD</span>
    </div>
  </main>
</body>
</html>
```